8 Page A6 booklet for Hypnosis/Hypnotherapy product

Please see PDF document attached for design brief. The booklet will be printed in http://www.pellavorn.co.uk/shop/brochures

If you do have any further questions please let me know.

This is going to be the insert for my DVD. The graphic for the DVD have now been attached to this project

Target Market(s)

People that have just purchased my Hypnosis CD

Industry/Entity Type

Hypnotherapy

Requirements
Must have
• I have attached a brief. Hopefully this explains but please do let me know if you have any further questions

```html
<!DOCTYPE html>
<html lang="en">
<head>
<meta charset="utf-8">
<title>Daniel Hartwell Hypnotherapy – Booklet Spread</title>
<link rel="stylesheet" href="https://fonts.googleapis.com/css2?family=Jost:wght@300;400;500;700&display=swap">
<style>
:root{
  --page-bg:#e9e4dc;
  --navy-deep:#23246a;
  --navy-mid:#1f3a86;
  --blue-bright:#1a55a3;
  --text-light:#ffffff;
  --rule:#c9d1ea;
  --sunset-warm:#c98a6a;
  --sunset-dusk:#5a4a86;
}
*{margin:0;padding:0;box-sizing:border-box}
html,body{width:1200px;height:1200px;overflow:hidden;background:var(--page-bg)}
body{font-family:"Jost",sans-serif;color:var(--text-light)}
.spread{position:absolute;left:174px;top:0;width:852px;height:1200px}
.page{position:absolute;left:0;width:852px;height:600px;overflow:hidden}
.page--profile{top:0;background:linear-gradient(200deg,var(--navy-deep) 0%,var(--navy-mid) 55%,var(--blue-bright) 100%)}
.page--faq{top:600px;background:linear-gradient(20deg,var(--blue-bright) 0%,var(--navy-mid) 35%,var(--navy-deep) 75%)}
.section{position:absolute;width:364px}
.section__title{font-weight:300;font-size:16.5px;letter-spacing:.4px;text-transform:uppercase;padding-bottom:7px;border-bottom:1px solid var(--rule)}
.section__body{font-size:10px;line-height:13.5px;letter-spacing:.2px;margin-top:36px}
.col-left{left:30px}
.col-right{left:458px}
.badges{position:absolute;left:30px;top:231px;display:flex;gap:28px;align-items:flex-start}
.badge{background:#fff;border:2px solid #1c1d55;width:104px;height:52px;border-radius:3px}
.badge--round{width:52px;height:52px;border-radius:50%;background:#3aa05a;border:none}
.portrait{position:absolute;left:70px;top:307px;width:311px;height:293px;border-radius:140px 140px 0 0;background:radial-gradient(ellipse at 50% 35%,#9a7a68 0%,#4a3d3a 45%,#2a2c3a 100%)}
.faq-list{margin-top:36px}
.faq-item{height:67.6px}
.faq-item__q{font-weight:700;font-size:10.5px;letter-spacing:.3px}
.faq-item__a{font-size:10px;line-height:13.5px;letter-spacing:.2px}
.scene{position:absolute;left:390px;top:0;width:462px;height:380px;background:radial-gradient(ellipse at 68% 58%,#e8a070 0%,var(--sunset-warm) 14%,var(--sunset-dusk) 42%,rgba(35,36,106,0) 75%)}
.offer{position:absolute;left:458px;top:396px;width:360px}
.offer__title{font-size:19px;line-height:24px;font-weight:400}
.offer__title strong{font-weight:700}
.offer__text{font-size:13.5px;line-height:17px;margin-top:30px}
.offer__code{font-size:10.5px;margin-top:18px}
.offer__url{font-size:10.5px;font-weight:700;margin-top:15px}
</style>
</head>
<body>
<div class="spread">
  <section class="page page--profile">
    <div class="section col-left" style="top:100px">
      <h2 class="section__title">Daniel Hartwell</h2>
      <p class="section__body">Daniel is a qualified and experienced Hypnotherapist who practices in Plymouth &amp; London. He is a member of the following professional governing bodies.</p>
    </div>
    <div class="badges">
      <div class="badge" role="img" aria-label="Professional association badge"></div>
      <div class="badge badge--round" role="img" aria-label="Professional council badge"></div>
    </div>
    <div class="portrait" role="img" aria-label="Portrait photograph of the hypnotherapist in a tweed jacket"></div>
    <div class="section col-right" style="top:100px">
      <h2 class="section__title">About Daniel</h2>
      <p class="section__body">Daniel is passionate about people and sees Hypnotherapy as the most effective tool for positively impacting on our hugely powerful brains. As well as ensuring that his techniques and practices are at the cutting edge of the latest developments into the brain, he also has a huge amount of life experience, including leading operations in highly stressful environments in his previous work with the Central Investigations Bureau and the National Security Office.</p>
    </div>
    <div class="section col-right" style="top:322px">
      <h2 class="section__title">Experience &amp; Qualifications</h2>
      <p class="section__body">Daniel is a fully qualified and insured Solution Focused Hypnotherapist. His products and services assist over 30,000 people every year and have reached more than 20 different countries. He is the producer of the first inflight Hypnotherapy channel in partnership with Skyline Airways. He has experience working with a wide variety of people including celebrities and high profile people. His client confidentiality is always of paramount importance.</p>
    </div>
  </section>

  <section class="page page--faq">
    <div class="scene" role="img" aria-label="Silhouette of a woman holding up a dreamcatcher against a sunset sky"></div>
    <div class="section col-left" style="top:100px">
      <h2 class="section__title">Frequently Asked Questions</h2>
      <div class="faq-list">
        <div class="faq-item"><p class="faq-item__q">ASK 1</p><p class="faq-item__a">Lorem ipsum dolor sit amet, modo integre ocurreret an sea, te ubique aperiri sanctus sit. Id cum nonumy concludaturque. Pro ne oblique constituam. Sed ne veniam graeco, est ex congue aperiam laboramus.</p></div>
        <div class="faq-item"><p class="faq-item__q">ASK 1</p><p class="faq-item__a">Lorem ipsum dolor sit amet, modo integre ocurreret an sea, te ubique aperiri sanctus sit. Id cum nonumy concludaturque. Pro ne oblique constituam. Sed ne veniam graeco, est ex congue aperiam laboramus.</p></div>
        <div class="faq-item"><p class="faq-item__q">ASK 1</p><p class="faq-item__a">Lorem ipsum dolor sit amet, modo integre ocurreret an sea, te ubique aperiri sanctus sit. Id cum nonumy concludaturque. Pro ne oblique constituam. Sed ne veniam graeco, est ex congue aperiam laboramus.</p></div>
        <div class="faq-item"><p class="faq-item__q">ASK 1</p><p class="faq-item__a">Lorem ipsum dolor sit amet, modo integre ocurreret an sea, te ubique aperiri sanctus sit. Id cum nonumy concludaturque. Pro ne oblique constituam. Sed ne veniam graeco, est ex congue aperiam laboramus.</p></div>
        <div class="faq-item"><p class="faq-item__q">ASK 1</p><p class="faq-item__a">Lorem ipsum dolor sit amet, modo integre ocurreret an sea, te ubique aperiri sanctus sit. Id cum nonumy concludaturque. Pro ne oblique constituam. Sed ne veniam graeco, est ex congue aperiam laboramus.</p></div>
        <div class="faq-item"><p class="faq-item__q">ASK 1</p><p class="faq-item__a">Lorem ipsum dolor sit amet, modo integre ocurreret an sea, te ubique aperiri sanctus sit. Id cum nonumy concludaturque. Pro ne oblique constituam. Sed ne veniam graeco, est ex congue aperiam laboramus.</p></div>
      </div>
    </div>
    <div class="offer">
      <p class="offer__title"><strong>Exclusive 50% off</strong><br>of your first download</p>
      <p class="offer__text">Go to the website and input the following code at checkout to get 50% off</p>
      <p class="offer__code">Code: exclusive50</p>
      <p class="offer__url">DanielHartwellHypnotherapy.com</p>
    </div>
  </section>
</div>
</body>
</html>
```